New Letterhead request for our Law Firm!

We are a small Estate Planning Firm who just got out logo redesigned. It's attached. We need some letterhead for our client welcome letters and so forth. Clean, bright, and approachable is our style. If you need the specifications for our color scheme or other versions of the logo file, we have those too. Visit our website to get an idea about our services/aesthetics:https://bramblecove.law/

Target Market(s)

Adults 30-80

Colors

Designer to choose colors to be used in the design.

Requirements
Must have
• Logo with color. Contact information

```html
<!DOCTYPE html>
<html lang="en">
<head>
<meta charset="utf-8">
<title>Bramblecove Law Firm — Letterhead</title>
<link href="https://fonts.googleapis.com/css2?family=Montserrat:wght@400;500;600&display=swap" rel="stylesheet">
<style>
  :root {
    --sage: #6b9385;
    --charcoal: #4a4a4b;
    --ink: #3a3a3a;
    --paper: #ffffff;
    --backdrop: #c9c9c9;
    --sig-fill: #eceeed;
  }
  * { box-sizing: border-box; margin: 0; padding: 0; }
  html, body { width: 1200px; height: 1200px; overflow: hidden; }
  body {
    background: var(--backdrop);
    font-family: "Montserrat", Arial, sans-serif;
    color: var(--ink);
    position: relative;
  }
  .sheet {
    position: absolute;
    top: 230px;
    width: 540px;
    height: 700px;
    background: var(--paper);
    box-shadow: 0 4px 18px rgba(0,0,0,0.18);
    overflow: hidden;
  }
  .sheet--blank { left: 40px; }
  .sheet--letter { left: 620px; }

  .brand {
    position: absolute;
    top: 34px; left: 30px;
    display: flex; align-items: center; gap: 10px;
  }
  .brand__mark {
    width: 42px; height: 42px; border-radius: 50%;
    border: 2px solid var(--sage);
  }
  .brand__name {
    color: var(--sage);
    font-weight: 600;
    line-height: 1.05;
    letter-spacing: 0.04em;
    text-transform: uppercase;
  }
  .brand__name span { display: block; }
  .brand__name .brand__primary { font-size: 19px; }
  .brand__name .brand__secondary { font-size: 10px; letter-spacing: 0.16em; }

  .contact {
    position: absolute;
    top: 34px; right: 30px;
    width: 150px;
    font-size: 8px;
    line-height: 1.45;
    color: var(--ink);
  }
  .contact__address { margin-bottom: 8px; }
  .contact__row { display: flex; align-items: center; gap: 6px; margin-bottom: 5px; }
  .contact__icon { width: 9px; height: 9px; flex: none; }

  .letter {
    position: absolute;
    top: 170px; left: 30px; right: 30px;
    font-size: 7.4px;
    line-height: 1.6;
  }
  .letter__date { color: var(--sage); font-size: 8px; font-weight: 500; margin-bottom: 10px; }
  .letter__recipient { font-size: 7px; line-height: 1.45; margin-bottom: 44px; }
  .letter__greeting { color: var(--sage); font-weight: 600; font-size: 8px; margin-bottom: 14px; }
  .letter p { text-align: justify; margin-bottom: 12px; }
  .signature {
    width: 180px; height: 44px; margin-top: 46px;
    background: var(--sig-fill); border-radius: 4px;
  }
  .signer__name { color: var(--sage); font-weight: 600; font-size: 8px; margin-top: 14px; }
  .signer__title { font-size: 6.5px; }

  .footer__band {
    position: absolute; left: 0; bottom: 0;
    width: 68%; height: 40px;
    background: var(--sage);
    color: #fff;
    font-size: 7.5px; font-weight: 500;
    letter-spacing: 0.06em;
    text-transform: uppercase;
    display: flex; align-items: center; padding-left: 44px;
  }
  .footer__notch {
    position: absolute; bottom: 0; left: 68%;
    width: 11%; height: 58px;
    background: var(--paper);
  }
  .footer__block {
    position: absolute; right: 0; bottom: 0;
    width: 21%; height: 46px;
    background: var(--charcoal);
  }
</style>
</head>
<body>

  <section class="sheet sheet--blank" aria-label="Blank letterhead">
    <header class="brand">
      <div class="brand__mark"></div>
      <div class="brand__name"><span class="brand__primary">Bramblecove</span><span class="brand__secondary">Law Firm</span></div>
    </header>
    <address class="contact" style="font-style:normal">
      <div class="contact__address">2480 Lakeview Parkway,<br>Suite 310, Maple Grove, MN 55369</div>
      <div class="contact__row"><svg class="contact__icon" viewBox="0 0 10 10"><circle cx="5" cy="5" r="5" fill="#6b9385"/><path d="M3.2 2.6l1 1-.6.7c.4.8 1 1.4 1.8 1.8l.7-.6 1 1-.7.8C4.6 7 3 5.4 2.6 3.3z" fill="#fff"/></svg>612 555 0148</div>
      <div class="contact__row"><svg class="contact__icon" viewBox="0 0 10 10"><circle cx="5" cy="5" r="5" fill="#6b9385"/><rect x="2.6" y="3.3" width="4.8" height="3.4" fill="#fff"/><path d="M2.6 3.3L5 5.2l2.4-1.9" stroke="#6b9385" stroke-width=".6" fill="none"/></svg>info@bramblecove.law</div>
      <div class="contact__row"><svg class="contact__icon" viewBox="0 0 10 10"><circle cx="5" cy="5" r="5" fill="#6b9385"/><circle cx="5" cy="5" r="2.4" stroke="#fff" stroke-width=".7" fill="none"/><path d="M2.6 5h4.8M5 2.6v4.8" stroke="#fff" stroke-width=".6"/></svg>www.bramblecove.law</div>
    </address>
    <footer>
      <div class="footer__band">Bramblecove Law Firm, PLLC | Daniel R. Whitcombe, Esq. © 2019</div>
      <div class="footer__notch"></div>
      <div class="footer__block"></div>
    </footer>
  </section>

  <section class="sheet sheet--letter" aria-label="Letterhead with sample letter">
    <header class="brand">
      <div class="brand__mark"></div>
      <div class="brand__name"><span class="brand__primary">Bramblecove</span><span class="brand__secondary">Law Firm</span></div>
    </header>
    <address class="contact" style="font-style:normal">
      <div class="contact__address">2480 Lakeview Parkway,<br>Suite 310, Maple Grove, MN 55369</div>
      <div class="contact__row"><svg class="contact__icon" viewBox="0 0 10 10"><circle cx="5" cy="5" r="5" fill="#6b9385"/><path d="M3.2 2.6l1 1-.6.7c.4.8 1 1.4 1.8 1.8l.7-.6 1 1-.7.8C4.6 7 3 5.4 2.6 3.3z" fill="#fff"/></svg>612 555 0148</div>
      <div class="contact__row"><svg class="contact__icon" viewBox="0 0 10 10"><circle cx="5" cy="5" r="5" fill="#6b9385"/><rect x="2.6" y="3.3" width="4.8" height="3.4" fill="#fff"/><path d="M2.6 3.3L5 5.2l2.4-1.9" stroke="#6b9385" stroke-width=".6" fill="none"/></svg>info@bramblecove.law</div>
      <div class="contact__row"><svg class="contact__icon" viewBox="0 0 10 10"><circle cx="5" cy="5" r="5" fill="#6b9385"/><circle cx="5" cy="5" r="2.4" stroke="#fff" stroke-width=".7" fill="none"/><path d="M2.6 5h4.8M5 2.6v4.8" stroke="#fff" stroke-width=".6"/></svg>www.bramblecove.law</div>
    </address>

    <article class="letter">
      <div class="letter__date">15.11.2019</div>
      <div class="letter__recipient">Priya Ramsden<br>48 Harbour Lane,<br>Elm Court, Brisbane,<br>Australia</div>
      <div class="letter__greeting">Dear Priya</div>
      <p>Lorem ipsum dolor sit amet, consectetur adipiscing elit. Quisque sagittis, sapien id placerat cursus, purus turpis ultrices lectus, a dictum tellus magna eget nulla. Nulla at tortor quis diam maximus tempus. Ut at dui eget lorem molestie elementum. Phasellus egestas metus a magna imperdiet, a vehicula sapien commodo. In tellus nisl, dapibus venenatis finibus nec, lobortis eu nisi. Curabitur pellentesque sapien sed erat ullamcorper aliquam. Morbi sed placerat nisi, ut elementum tellus.</p>
      <p>Proin laoreet dui vel congue cursus. Duis ultricies neque quis sapien rutrum, id euismod nunc hendrerit. Nulla euismod quam nibh, ut elementum tortor finibus eget. Nunc tempor libero placerat mauris aliquet euismod. Integer in mauris nec neque elementum iaculis.</p>
      <p>Donec suscipit nunc in nisl imperdiet, vitae egestas justo tempus. Vivamus pretium congue gravida. Curabitur ornare est ac tellus malesuada dictum. Quisque eget enim hendrerit, porttitor urna vitae, varius enim. In tempus sit amet arcu eget auctor. Maecenas posuere pharetra massa id malesuada.</p>
      <p>Duis ultricies neque quis sapien rutrum, id euismod nunc hendrerit. Nulla euismod quam nibh, ut elementum tortor finibus eget. Nunc tempor libero placerat mauris aliquet euismod. Integer in mauris nec neque elementum iaculis.</p>
      <div class="signature" role="img" aria-label="Handwritten signature of the attorney"></div>
      <div class="signer__name">Thomas Everly</div>
      <div class="signer__title">Attorney/Lawyer</div>
    </article>

    <footer>
      <div class="footer__band">Bramblecove Law Firm, PLLC | Daniel R. Whitcombe, Esq. © 2019</div>
      <div class="footer__notch"></div>
      <div class="footer__block"></div>
    </footer>
  </section>

</body>
</html>
```